Bluebird Listings ad 2014 15

I need a design for an advertisement in our Bluebird Listings book telephone directory.
The directory runs for a 12 month period.

Our business offers 24 hour glass replacements to homes, shops and offices.
Our service is usually required by customers that require their glass replaced urgently
.
The ad is 1 of many in the directory offering the same service so we need to attract the customers attention quickly and easily and deliver our message - "24hr glass replacements to doors windows and shopfronts. Call now 9372 4816".

I want to keep the data in the attached ad but with a professional graphic presentation.

The ad size is 58mm high x 83mm wide, full colour.

Target Market(s)

Our customer is generally someone in need of an emergency repair. They aren't spending time shopping around for a product, they have a problem that they want fixed promptly and professionally.

Industry/Entity Type

Business

Font styles to use
Sans Serif

Colors
0255a3
f37022

Requirements
Must have
• "24HR" must stand out, this is a key aspect of our service. The ad needs to be clear and easy to read.

```html
<!DOCTYPE html>
<html lang="en">
<head>
<meta charset="utf-8">
<title>Steadfast Glass – 24hr Glass Replacement</title>
<link href="https://fonts.googleapis.com/css2?family=Bowlby+One&family=Montserrat:wght@800&family=Open+Sans:wght@600;700&display=swap" rel="stylesheet">
<style>
  :root {
    --blue: #0255a3;
    --blue-deep: #013f7a;
    --blue-mid: #3f86c9;
    --blue-light: #dbeaf8;
    --orange: #f37022;
    --orange-deep: #d85a10;
    --orange-pale: #fde6d6;
    --white: #ffffff;
    --ink: #111111;
  }
  * { margin: 0; padding: 0; box-sizing: border-box; }
  html, body { width: 1200px; height: 839px; overflow: hidden; background: var(--white); }
  .ad {
    position: relative;
    width: 1200px;
    height: 839px;
    overflow: hidden;
    font-family: "Open Sans", Arial, sans-serif;
  }
  .ad__backdrop { position: absolute; inset: 0; }
  .headline {
    position: absolute; left: 0; top: 6px; width: 1200px; height: 120px;
  }
  .headline text {
    font-family: "Bowlby One", "Arial Black", sans-serif;
    font-size: 100px;
    fill: var(--orange);
    stroke: var(--white);
    stroke-width: 6px;
    paint-order: stroke;
  }
  .subhead {
    position: absolute; left: 0; top: 124px; width: 1200px;
    text-align: center; color: var(--white);
    font-weight: 600; font-size: 56px; letter-spacing: 1px; line-height: 1;
  }
  .service-tag {
    position: absolute;
    width: 420px; height: 74px;
    background: var(--white);
    box-shadow: 4px 6px 8px rgba(0,0,0,0.25);
    color: var(--blue);
    font-weight: 700; font-size: 38px; line-height: 74px;
    text-align: center;
  }
  .service-tag--door { left: 72px; top: 232px; transform: rotate(1.5deg); }
  .service-tag--window { left: 72px; top: 328px; transform: rotate(-2deg); }
  .service-tag--shopfront { left: 712px; top: 230px; transform: rotate(-1.5deg); }
  .service-tag--shower { left: 712px; top: 330px; transform: rotate(2deg); }
  .badge { position: absolute; left: 496px; top: 228px; width: 210px; height: 200px; }
  .badge text { font-family: "Montserrat", Arial, sans-serif; font-weight: 800; fill: var(--white); }
  .safety-line {
    position: absolute; left: 0; top: 440px; width: 1200px;
    text-align: center; color: var(--blue);
    font-weight: 700; font-size: 40px; line-height: 46px; letter-spacing: 0.5px;
  }
  .safety-line strong { color: var(--orange-deep); font-weight: 700; }
  .call-line {
    position: absolute; left: 0; top: 550px; width: 1200px;
    text-align: center; color: var(--white);
    font-family: "Montserrat", Arial, sans-serif; font-weight: 800;
    font-size: 62px; letter-spacing: 4px; line-height: 1;
  }
  .trust-line {
    position: absolute; left: 0; top: 610px; width: 1200px;
    text-align: center; color: var(--white);
    font-weight: 600; font-size: 34px; line-height: 1;
  }
  .brand-name {
    position: absolute; left: 0; top: 670px; width: 1200px;
    text-align: center; color: var(--white);
    font-weight: 600; font-size: 42px; line-height: 1;
  }
  .tagline {
    position: absolute; left: 0; top: 720px; width: 1200px;
    text-align: center; color: var(--white);
    font-weight: 600; font-size: 42px; line-height: 1;
    transform: rotate(-2deg);
  }
  .insurance-line {
    position: absolute; left: 0; top: 796px; width: 1200px;
    text-align: center; color: var(--blue-deep);
    font-weight: 700; font-size: 30px; line-height: 1;
  }
</style>
</head>
<body>
<main class="ad">
  <svg class="ad__backdrop" width="1200" height="839" viewBox="0 0 1200 839" aria-hidden="true">
    <defs>
      <radialGradient id="burst" cx="0.5" cy="0" r="0.8">
        <stop offset="0" style="stop-color:var(--blue-mid)"/>
        <stop offset="0.45" style="stop-color:var(--blue)"/>
        <stop offset="1" style="stop-color:var(--blue-deep)"/>
      </radialGradient>
      <radialGradient id="skyGlow" cx="0.5" cy="0.55" r="0.6">
        <stop offset="0" style="stop-color:var(--white)"/>
        <stop offset="0.45" style="stop-color:var(--blue-light)"/>
        <stop offset="1" style="stop-color:var(--blue-mid)"/>
      </radialGradient>
    </defs>
    <rect x="0" y="150" width="1200" height="285" fill="url(#skyGlow)"/>
    <path d="M0 0 H1200 V206 Q600 166 0 228 Z" fill="var(--orange)"/>
    <path d="M0 0 H1200 V194 Q600 154 0 214 Z" fill="url(#burst)" role="img" aria-label="Shattered glass burst"/>
    <rect x="0" y="433" width="1200" height="105" fill="var(--white)"/>
    <rect x="0" y="538" width="1200" height="120" fill="var(--orange)"/>
    <rect x="0" y="658" width="1200" height="181" fill="var(--orange-pale)"/>
    <path d="M0 662 H1200 V772 Q600 800 0 784 Z" fill="var(--blue)"/>
    <line x1="0" y1="660" x2="1200" y2="660" stroke="var(--white)" stroke-width="4"/>
  </svg>

  <svg class="headline" viewBox="0 0 1200 120" role="heading" aria-level="1">
    <text x="90" y="104" textLength="1020" lengthAdjust="spacingAndGlyphs">BROKEN GLASS?</text>
  </svg>
  <p class="subhead">WE CAN REPLACE IT</p>

  <div class="service-tag service-tag--door">DOOR GLASS</div>
  <div class="service-tag service-tag--window">WINDOW GLASS</div>
  <div class="service-tag service-tag--shopfront">SHOPFRONT GLASS</div>
  <div class="service-tag service-tag--shower">SHOWER GLASS</div>

  <svg class="badge" viewBox="0 0 210 200" role="img" aria-label="24 hour service">
    <circle cx="105" cy="100" r="96" fill="var(--white)"/>
    <circle cx="105" cy="100" r="88" fill="var(--orange)"/>
    <text x="105" y="86" text-anchor="middle" font-size="72">24</text>
    <text x="105" y="140" text-anchor="middle" font-size="46">HR</text>
    <rect x="6" y="155" width="198" height="40" fill="var(--white)"/>
    <rect x="12" y="160" width="186" height="30" fill="var(--blue)"/>
    <text x="105" y="184" text-anchor="middle" font-size="25" letter-spacing="1">SERVICE</text>
  </svg>

  <p class="safety-line">To regain the <strong>SAFETY</strong> and <strong>SECURITY</strong><br>in your Home, Shop or Office</p>

  <p class="call-line">CALL: 9372 48 16</p>
  <p class="trust-line">Qualified tradesmen | All work guaranteed</p>

  <p class="brand-name">steadfast GLASS</p>
  <p class="tagline">The trusted name in Glass replacement</p>
  <p class="insurance-line">Insurance Billed Direct</p>
</main>
</body>
</html>
```